Business Card Design

We need a business card designed for a new company based in Melbourne called KPo solutions. KPo solutions provides management consulting specialising in the health and social services sector.

KPo solutions offer a unique set of specialist skills │dealing with all levels of government │ unique communication skills│intimate knowledge of the health sector │solutions tailored to unique circumstances.

KPo solutions takes on a select number of clients at any one time, this ensures that your organisation receives the attention required. On larger projects, KPo solutions join up with other consultants to bring specialist skills to a project.
Updates

This is the first time I have used Pattern Hive and thank you all for responding. The variation is amazing and makes it hard to decide. I have to ask some of my friends to give me their views. The response is fantastic. The one I pick will basically be the most visually appealing

Industry/Entity Type

Management Consulting

Contact Information for Business Card

Martin Hollis, Principal, KPo solutions, 14 Calloway Ave, Westbridge VIC 3094, 0438 712 304, martinh@kposolutions.com.au, www.kposolutions.com.au

```html
<!DOCTYPE html>
<html lang="en">
<head>
<meta charset="utf-8">
<title>KPo solutions – Business Card</title>
<link rel="stylesheet" href="https://fonts.googleapis.com/css2?family=Open+Sans:wght@400;700&family=Roboto:wght@400&family=Roboto+Slab:wght@600&display=swap">
<style>
  :root {
    --page: #ffffff;
    --card-red: #bc1a29;
    --brand-red: #b91f26;
    --band-tint: rgba(255, 255, 255, 0.055);
    --card-edge: #3a3a3a;
    --ink-light: #ffffff;
    --tagline: #f4dede;
  }
  html, body {
    margin: 0;
    width: 1200px;
    height: 1000px;
    overflow: hidden;
    background: var(--page);
  }
  .card {
    position: absolute;
    left: 74px;
    top: 189px;
    width: 1052px;
    height: 601px;
    background: var(--card-red);
    outline: 1.5px solid var(--card-edge);
    overflow: hidden;
    color: var(--ink-light);
  }
  .band {
    position: absolute;
    background: var(--band-tint);
  }
  .band--v1 { left: 231px; top: 187px; width: 99px; height: 414px; }
  .band--h1 { left: 0; top: 396px; width: 559px; height: 98px; }
  .band--v2 { left: 721px; top: 0; width: 98px; height: 601px; }
  .band--h2 { left: 491px; top: 186px; width: 561px; height: 96px; }

  .brand {
    position: absolute;
    left: 0;
    top: 0;
    width: 609px;
    height: 187px;
    background: var(--brand-red);
  }
  .brand__name {
    position: absolute;
    left: 30px;
    top: 18px;
    margin: 0;
    font-family: "Open Sans", sans-serif;
    font-weight: 700;
    font-size: 68px;
    line-height: 1.2;
    letter-spacing: 1px;
  }
  .brand__tagline {
    position: absolute;
    left: 115px;
    top: 139px;
    margin: 0;
    font-family: "Roboto Slab", serif;
    font-weight: 600;
    font-size: 18px;
    letter-spacing: 1.2px;
    text-transform: uppercase;
    color: var(--tagline);
  }
  .person {
    position: absolute;
    left: 28px;
    top: 224px;
  }
  .person__name {
    margin: 0;
    font-family: "Open Sans", sans-serif;
    font-weight: 700;
    font-size: 40px;
    line-height: 50px;
  }
  .person__role {
    margin: 0;
    font-family: "Roboto", sans-serif;
    font-size: 30px;
    line-height: 42px;
  }
  .contact {
    position: absolute;
    left: 542px;
    top: 296px;
    margin: 0;
    padding: 0;
    list-style: none;
    font-family: "Roboto", sans-serif;
    font-size: 31px;
    line-height: 50.7px;
  }
  .contact__item {
    position: relative;
    padding-left: 37px;
  }
  .contact__icon {
    position: absolute;
    left: 2px;
    top: 14px;
    width: 20px;
    height: 20px;
    fill: var(--ink-light);
  }
</style>
</head>
<body>
  <main class="card">
    <div class="band band--v1"></div>
    <div class="band band--h1"></div>
    <div class="band band--v2"></div>
    <div class="band band--h2"></div>

    <header class="brand">
      <h1 class="brand__name">KPo solutions</h1>
      <p class="brand__tagline">Health &amp; Social Services Consulting</p>
    </header>

    <section class="person">
      <h2 class="person__name">Martin Hollis</h2>
      <p class="person__role">Principal</p>
    </section>

    <ul class="contact">
      <li class="contact__item">
        <svg class="contact__icon" viewBox="0 0 20 20" aria-hidden="true"><path d="M10 1a6 6 0 0 0-6 6c0 4.5 6 11 6 11s6-6.5 6-11a6 6 0 0 0-6-6zm0 8.3A2.3 2.3 0 1 1 10 4.7a2.3 2.3 0 0 1 0 4.6z"/></svg>
        14 Calloway Ave<br>Westbridge 3094
      </li>
      <li class="contact__item">
        <svg class="contact__icon" viewBox="0 0 20 20" aria-hidden="true"><path d="M5 1h10v18H5zM6.5 3v11h7V3z M9 15.5h2v2H9z" fill-rule="evenodd"/></svg>
        +0438 712 304
      </li>
      <li class="contact__item">
        <svg class="contact__icon" viewBox="0 0 20 20" aria-hidden="true"><text x="10" y="15" text-anchor="middle" font-family="Roboto, sans-serif" font-size="15">@</text></svg>
        martinh@kposolutions.com.au
      </li>
      <li class="contact__item">
        <svg class="contact__icon" viewBox="0 0 20 20" aria-hidden="true"><circle cx="10" cy="10" r="8.5"/><g stroke="#bc1a29" stroke-width="1.2" fill="none"><ellipse cx="10" cy="10" rx="3.5" ry="8.5"/><line x1="1.5" y1="10" x2="18.5" y2="10"/><line x1="3" y1="6" x2="17" y2="6"/><line x1="3" y1="14" x2="17" y2="14"/></g></svg>
        www.kposolutions.com.au
      </li>
    </ul>
  </main>
</body>
</html>
```